Larkmere Hall Business Cards design with a logo

I want two Business cards designed with a very modern contemporary logo UNING 1920'S FONT STYLES with the following details

Address:
Larkmere Hall
17 Penwick Lane
Helensburgh
K31 5TB

Details for card 1

Name: Desmond Hartley
email: Desmond.hartley@larkmere.example
Tel : +971 55 318 2964
Tel +44 7700 900 318

Details Card 2

Name: Desmond Hartley
email: Oliver.brandt@larkmere.example
Tel : +971 55 604 1387

Larkmere hall is a house that was built around 1880 and was used extensively in the 1920's for entertaining and parties in the arts scene, the house again will be resurrected to a modern entertainment venue

If you have any questions feel free to ask

Target Market(s)

The market for this is the young modern crowd

Industry/Entity Type

Entertainment Industry

Contact Information for Business Card

Address:
Larkmere Hall
17 Penwick Lane
Helensburgh
K31 5TB

Details for card 1

Name: Desmond Hartley
Tel : +971 55 318 2964
Tel +44 7700 900 318

Details Card 2

Name: Oliver Brandt
Tel : +971 55 604 1387

Logo Text

Larkmere Hall

Font styles to use
Other font styles liked:
• 1920'S FONT STULES

Requirements
Must have
• Modern Contemporary, whilst taking into consideration the age of the house as detailed above. YOU MUT BE USING 1920'S FONT STYLES
Nice to have
• 1920'S FONT STYLES see attached image if a suggestion
Should not have
• Should not look old or dated

```html
<!DOCTYPE html>
<html lang="en">
<head>
<meta charset="utf-8">
<title>Larkmere Hall Business Cards</title>
<link rel="stylesheet" href="https://fonts.googleapis.com/css2?family=Federo&family=Poiret+One&display=swap">
<style>
  :root {
    --teal: #4aaba6;
    --white: #ffffff;
    --house-tone: linear-gradient(160deg, #ffffff 0%, #e4f3f2 100%);
    --house-tone-teal: linear-gradient(160deg, #5cb6b1 0%, #4aaba6 100%);
  }
  * { margin: 0; padding: 0; box-sizing: border-box; }
  html, body { width: 769px; height: 1200px; overflow: hidden; background: var(--white); }
  .sheet { position: relative; width: 769px; height: 1200px; font-family: "Federo", sans-serif; color: var(--teal); }

  .card-back { position: absolute; left: 0; top: 0; width: 769px; height: 395px; background: var(--teal); color: var(--white); text-align: center; }
  .house-art { position: absolute; border-radius: 2px; }
  .card-back .house-art { left: 290px; top: 80px; width: 188px; height: 104px; background: var(--house-tone); }
  .wordmark { font-family: "Poiret One", sans-serif; font-weight: 400; letter-spacing: 1px; line-height: 1; white-space: nowrap; }
  .card-back .wordmark { position: absolute; left: 0; right: 0; top: 206px; font-size: 57px; }
  .address { position: absolute; left: 0; right: 0; top: 278px; font-size: 24px; line-height: 30.5px; }

  .card-front { position: absolute; left: 0; width: 769px; height: 400px; }
  .card-front.first { top: 400px; }
  .card-front.second { top: 801px; }
  .person { position: absolute; left: 30px; line-height: 1; white-space: nowrap; }
  .person .name { position: absolute; top: 134px; font-size: 46px; }
  .person .contact { position: absolute; top: 208px; font-size: 22px; line-height: 35px; }
  .second .person .contact { top: 217px; }
  .card-front .house-art { left: 457px; top: 95px; width: 284px; height: 159px; background: var(--house-tone-teal); }
  .card-front .wordmark { position: absolute; left: 437px; width: 324px; text-align: center; top: 276px; font-size: 37px; }
  .second .wordmark { top: 279px; }
</style>
</head>
<body>
<main class="sheet">
  <section class="card-back">
    <div class="house-art" role="img" aria-label="White silhouette illustration of the Victorian house"></div>
    <h1 class="wordmark">LARKMERE HALL</h1>
    <p class="address">17 Penwick Lane<br>Helensburgh<br>K31 5TB</p>
  </section>

  <section class="card-front first">
    <div class="person">
      <h2 class="name">Desmond Hartley</h2>
      <p class="contact">Desmond.hartley@larkmere.example<br>971 55 318 2964<br>44 7700 900 318</p>
    </div>
    <div class="house-art" role="img" aria-label="Teal silhouette illustration of the Victorian house"></div>
    <p class="wordmark">LARKMERE HALL</p>
  </section>

  <section class="card-front second">
    <div class="person">
      <h2 class="name">Oliver Brandt</h2>
      <p class="contact">Oliver.brandt@larkmere.example<br>971 55 604 1387</p>
    </div>
    <div class="house-art" role="img" aria-label="Teal silhouette illustration of the Victorian house"></div>
    <p class="wordmark">LARKMERE HALL</p>
  </section>
</main>
</body>
</html>
```